professional business card

A Clean looking business card for a money transfer company. Our company is call Velorix= Transfer + Send = Transcend (next level)
to show professionalism as well as some effects to show digital tech.

1 side to have position, name and address
2 side to have company name and show that we provide money exchange and cross-border money transfer

Target Market(s)

Remittance companies and high net worth individuals

Industry/Entity Type

Finance

Contact Information for Business Card

Name, address, email, title, services- money exchange and cross-border remittance

Requirements
Nice to have
• Digital age feel

```html
<!DOCTYPE html>
<html lang="en">
<head>
<meta charset="utf-8">
<title>Velorix Business Card</title>
<link href="https://fonts.googleapis.com/css2?family=Montserrat:wght@400;500;600&family=Nunito+Sans:wght@400;700&display=swap" rel="stylesheet">
<style>
  :root {
    --canvas: #e6e6e6;
    --navy-dark: #1e2935;
    --navy-light: #35444f;
    --paper: #f1f1f1;
    --paper-shade: #e7e7e7;
    --teal: #5bb4c2;
    --ink: #25303b;
    --white: #f4f5f6;
  }
  * { margin: 0; padding: 0; box-sizing: border-box; }
  html, body {
    width: 1200px; height: 1200px; overflow: hidden;
    background: var(--canvas);
  }
  .canvas { position: relative; width: 1200px; height: 1200px; }
  .card {
    position: absolute; left: 234px; width: 731px; height: 418px;
    box-shadow: 0 6px 14px rgba(0,0,0,0.18);
  }
  .card-front {
    top: 160px;
    background: linear-gradient(200deg, var(--navy-light) 0%, var(--navy-dark) 75%);
  }
  .wordmark {
    position: absolute; left: 0; right: 0; top: 168px;
    text-align: center;
    font-family: "Montserrat", sans-serif; font-weight: 600;
    font-size: 52px; letter-spacing: 1px; line-height: 52px;
    color: var(--white);
  }
  .tagline {
    position: absolute; left: 0; right: 0; top: 356px;
    text-align: center;
    font-family: "Montserrat", sans-serif; font-weight: 400;
    font-size: 17px; color: var(--white); letter-spacing: 0.2px;
  }
  .card-back {
    top: 632px;
    background: linear-gradient(160deg, var(--paper-shade) 0%, var(--paper) 55%, var(--paper-shade) 100%);
  }
  .back-mark {
    position: absolute; left: 60px; top: 170px; width: 290px;
    text-align: center;
    font-family: "Montserrat", sans-serif; font-weight: 600;
    font-size: 48px; line-height: 56px; letter-spacing: 1px;
    color: var(--teal);
  }
  .contact {
    position: absolute; left: 397px; top: 106px;
    font-family: "Nunito Sans", sans-serif; color: var(--ink);
  }
  .contact-name { font-weight: 700; font-size: 24px; line-height: 30px; color: var(--teal); }
  .contact-title { font-size: 18px; line-height: 24px; margin-top: 0; }
  .contact-address { font-size: 18px; line-height: 26px; margin-top: 4px; }
  .contact-lines { list-style: none; margin-top: 10px; }
  .contact-lines li {
    display: flex; align-items: center; gap: 7px;
    font-size: 18px; line-height: 28px;
  }
  .contact-lines svg { width: 16px; height: 16px; flex: none; fill: var(--teal); }
</style>
</head>
<body>
<div class="canvas">
  <section class="card card-front">
    <div class="wordmark">VELORIX</div>
    <p class="tagline">Money Exchange And Cross-border Remittance</p>
  </section>

  <section class="card card-back">
    <div class="back-mark">VELORIX</div>
    <div class="contact">
      <div class="contact-name">Marcus Ellery</div>
      <div class="contact-title">Owner</div>
      <div class="contact-address">218 Harlow Street, 4th Floor,<br>Brookfield, NY 10234</div>
      <ul class="contact-lines">
        <li>
          <svg viewBox="0 0 16 16" aria-hidden="true"><path d="M3.2 1.5l2.3 2.6-1.2 1.6c.9 2 2.4 3.5 4.4 4.4l1.6-1.2 2.6 2.3-1.3 2.2C6.3 13.1 2.9 9.7 1.2 4.4z"/></svg>
          (555) 214-6830
        </li>
        <li>
          <svg viewBox="0 0 16 16" aria-hidden="true"><path d="M1 3.5h14v1L8 9 1 4.5z"/><path d="M1 6l7 4.5L15 6v6.5H1z"/></svg>
          info@velorix.com
        </li>
        <li>
          <svg viewBox="0 0 16 16" aria-hidden="true"><circle cx="8" cy="8" r="7" fill="none" stroke="#5bb4c2" stroke-width="1.6"/><path d="M4 4.5c1.5 0 2.5 1 2 2.3-.6 1.2.8 2 .3 3.4-.3.9-1 1.6-1.5 2.3C3.4 11 2.6 8.5 4 4.5zM10 3c1 .8.3 1.8 1.3 2.6.9.6 2 .3 2.4 1.5-.7 1.5-2 1.4-2.6 2.8-.3.7-1 .5-1.2-.4-.4-1.6-1.8-2-1.3-3.6z"/></svg>
          www.velorix.com
        </li>
      </ul>
    </div>
  </section>
</div>
</body>
</html>
```